Photojournalism/photography business needs a simple, timeless & professional letterhead design

We need a letterhead design for photography/photojournalism business called 'qolvb', no capitals.

The letterhead needs to be:
- simple
- professional
- timeless
- easy to read
- consists of at least 2 colors to make it stands out.

We do mainly editorial photography, photo articles for various publications, travel, businesses, as well as people such as family and kids.

The final design should communicate professionalism, easy identification, attention grabbing, even if it has to be found among a stack of various papers on the clients' desks.

Target Market(s)

Various publications.

Industry/Entity Type

Business

Requirements
Must have
• Please use the logo attached.

```html
<!DOCTYPE html>
<html lang="en">
<head>
<meta charset="utf-8">
<title>qolvb — letterhead concepts</title>
<link href="https://fonts.googleapis.com/css2?family=Nunito:wght@800&display=swap" rel="stylesheet">
<style>
  :root {
    --sky: #00b7f1;
    --ink: #3d3d3d;
    --paper: #ffffff;
    --edge: #bdbdbd;
  }
  html, body {
    margin: 0;
    padding: 0;
    width: 1200px;
    height: 1000px;
    overflow: hidden;
    background: var(--paper);
  }
  .board {
    position: relative;
    width: 1200px;
    height: 1000px;
    font-family: "Nunito", Arial, sans-serif;
  }
  .sheet {
    position: absolute;
    width: 242px;
    height: 341px;
    box-sizing: border-box;
    overflow: hidden;
    background: var(--paper);
  }
  .sheet--outlined { border: 1px solid var(--edge); }
  .sheet--solid { background: var(--sky); }
  .sheet--framed { border: 9px solid var(--sky); }

  .wordmark {
    position: absolute;
    margin: 0;
    font-weight: 800;
    line-height: 1;
    letter-spacing: -0.5px;
    white-space: nowrap;
  }
  .wordmark--ink { color: var(--ink); }
  .wordmark--sky { color: var(--sky); }
  .wordmark--center { left: 50%; transform: translateX(-50%); }

  .wordmark--giant {
    left: -8px;
    top: 70px;
    font-size: 150px;
    letter-spacing: -6px;
    color: var(--sky);
  }

  .contact-tab {
    position: absolute;
    right: 18px;
    bottom: 30px;
    width: 98px;
    height: 52px;
  }
  .contact-tab__lines {
    position: absolute;
    right: 4px;
    top: 17px;
    margin: 0;
    font-family: Arial, sans-serif;
    font-size: 3.6px;
    line-height: 5.6px;
    font-weight: 700;
    text-align: right;
    color: var(--paper);
  }
</style>
</head>
<body>
<main class="board">

  <section class="sheet sheet--solid" style="left:105px; top:144px;">
    <p class="wordmark wordmark--ink wordmark--center" style="top:137px; font-size:26px;">qolvb</p>
  </section>

  <section class="sheet sheet--framed" style="left:355px; top:144px;">
    <p class="wordmark wordmark--ink wordmark--center" style="top:124px; font-size:36px;">qolvb</p>
  </section>

  <section class="sheet sheet--outlined" style="left:604px; top:144px;">
    <p class="wordmark wordmark--giant">qolvb</p>
  </section>

  <section class="sheet sheet--outlined" style="left:853px; top:144px;">
    <p class="wordmark wordmark--sky wordmark--center" style="top:115px; font-size:36px;">qolvb</p>
  </section>

  <section class="sheet sheet--outlined" style="left:355px; top:512px;">
    <p class="wordmark wordmark--sky" style="left:34px; top:24px; font-size:26px;">qolvb</p>
    <div class="contact-tab">
      <svg width="98" height="52" viewBox="0 0 98 52" aria-hidden="true">
        <line x1="0" y1="51" x2="49" y2="2" stroke="var(--ink)" stroke-width="1"/>
        <polygon points="44,14 98,14 98,46 14,46" fill="var(--ink)"/>
      </svg>
      <p class="contact-tab__lines">+00 123 4567<br>www.qolvb.com<br>info@qolvb.com<br>12 Harbour Road, Bay City 00000</p>
    </div>
  </section>

  <section class="sheet sheet--outlined" style="left:604px; top:512px;">
    <p class="wordmark wordmark--ink" style="left:34px; top:24px; font-size:26px;">qolvb</p>
    <div class="contact-tab">
      <svg width="98" height="52" viewBox="0 0 98 52" aria-hidden="true">
        <line x1="0" y1="51" x2="49" y2="2" stroke="var(--ink)" stroke-width="1"/>
        <polygon points="44,14 98,14 98,46 14,46" fill="var(--sky)"/>
      </svg>
      <p class="contact-tab__lines">+00 123 4567<br>www.qolvb.com<br>info@qolvb.com<br>12 Harbour Road, Bay City 00000</p>
    </div>
  </section>

</main>
</body>
</html>
```